Medical VIP club - small design

Please read the specs in a design brief attached. Also we don't have logo in a Vector format and attaching the only version we have.

Industry/Entity Type

Club

```html
<!DOCTYPE html>
<html lang="en">
<head>
<meta charset="utf-8">
<title>Vitalis — VIP Club</title>
<link rel="stylesheet" href="https://fonts.googleapis.com/css2?family=Great+Vibes&family=Cormorant+Garamond:ital,wght@1,600&family=Noto+Serif:ital,wght@0,400;0,700;1,400;1,700&display=swap">
<style>
  :root {
    --page-bg: #7b6a4d;
    --page-bg-dark: #6c5c42;
    --frame: #8a7656;
    --frame-edge: #5f4f38;
    --ribbon-light: #c9a266;
    --ribbon-mid: #9c7440;
    --ribbon-dark: #6e4d25;
    --tab-top: #8f7a58;
    --tab-bottom: #6f5d42;
    --tab-active-top: #a38d68;
    --tab-active-bottom: #7f6b4c;
    --strip: #8b6a37;
    --strip-edge: #6e5126;
    --thumb-frame: #7e6a4c;
    --text-light: #fbf6ea;
    --text-soft: #e8dcc4;
  }
  * { margin: 0; padding: 0; box-sizing: border-box; }
  html, body { width: 1200px; height: 669px; overflow: hidden; }
  body {
    position: relative;
    background: radial-gradient(ellipse at 50% 40%, var(--page-bg) 0%, var(--page-bg-dark) 100%);
    font-family: "Noto Serif", Georgia, serif;
    color: var(--text-light);
  }
  .corner-ornament {
    position: absolute; top: 0; width: 170px; height: 669px;
    background: linear-gradient(180deg, rgba(210,190,150,.28), rgba(210,190,150,.08) 30%, rgba(210,190,150,0) 60%, rgba(210,190,150,.18));
  }
  .corner-ornament--left { left: 140px; }
  .corner-ornament--right { right: 100px; }

  .brand { position: absolute; left: 210px; top: 38px; display: flex; align-items: center; gap: 8px; }
  .brand__dot { width: 16px; height: 16px; border-radius: 50%; background: var(--text-light); }
  .brand__name { font-weight: 700; font-size: 30px; color: var(--text-light); letter-spacing: .5px; }

  .phone { position: absolute; right: 201px; top: 60px; font-style: italic; font-weight: 700; font-size: 13px; color: var(--text-light); }

  .nav-ribbon { position: absolute; left: 111px; top: 80px; width: 978px; height: 56px; }
  .main-nav { position: absolute; left: 0; top: 0; width: 1200px; height: 140px; }
  .main-nav a {
    position: absolute; top: 96px; height: 28px;
    display: flex; align-items: center; justify-content: center;
    font-family: "Cormorant Garamond", serif; font-style: italic; font-weight: 600;
    font-size: 16px; color: var(--text-light); text-decoration: none;
    background: linear-gradient(var(--tab-top), var(--tab-bottom));
    border: 1px solid var(--frame-edge); border-bottom: none; border-radius: 4px 4px 0 0;
    box-shadow: inset 0 1px 0 rgba(255,255,255,.2);
  }
  .main-nav a.is-active { top: 87px; height: 40px; padding-top: 10px; background: linear-gradient(var(--tab-active-top), var(--tab-active-bottom)); }

  .hero-frame {
    position: absolute; left: 171px; top: 124px; width: 858px; height: 352px;
    background: var(--frame); border: 1px solid var(--frame-edge);
    box-shadow: 0 2px 6px rgba(0,0,0,.35);
  }
  .hero-photo {
    position: absolute; left: 6px; top: 6px; width: 844px; height: 337px;
    background:
      radial-gradient(ellipse at 20% 35%, #fff7e4 0%, rgba(255,247,228,0) 30%),
      linear-gradient(180deg, #d9c39c 0%, #cfb07a 45%, #b98d4f 75%, #8c6434 100%);
  }
  .hero-caption { position: absolute; right: 42px; top: 62px; text-align: right; }
  .hero-caption h1 {
    font-family: "Great Vibes", cursive; font-weight: 400; font-size: 54px; line-height: 1;
    color: #fffdf7; text-shadow: 1px 1px 2px rgba(90,60,20,.5);
  }
  .hero-caption p {
    margin-top: 6px; font-style: italic; font-weight: 700; font-size: 12px; line-height: 13px;
    color: #fffdf7; text-shadow: 1px 1px 2px rgba(90,60,20,.6);
  }
  .slider-arrow {
    position: absolute; top: 156px; width: 43px; height: 35px;
    border: 1px solid rgba(255,255,255,.45); border-radius: 4px;
    background: rgba(120,100,70,.25);
    display: flex; align-items: center; justify-content: center;
  }
  .slider-arrow--prev { left: 4px; opacity: .55; }
  .slider-arrow--next { right: 4px; background: rgba(90,70,45,.35); }

  .gallery-strip {
    position: absolute; left: 159px; top: 470px; width: 882px; height: 134px;
    background: linear-gradient(var(--strip), #7d5e2e);
    border: 1px solid var(--strip-edge);
    box-shadow: 0 2px 5px rgba(0,0,0,.35);
  }
  .thumb {
    position: absolute; top: 12px; width: 166px; height: 117px;
    background: var(--thumb-frame); border-radius: 3px; padding: 5px;
    box-shadow: inset 0 0 0 1px rgba(0,0,0,.25);
  }
  .thumb__image { width: 100%; height: 100%; }
  .thumb--hospital { left: 19px; }
  .thumb--hospital .thumb__image { background: linear-gradient(160deg, #d8d0c2, #8e8170 55%, #4e4335); }
  .thumb--flight { left: 189px; }
  .thumb--flight .thumb__image { background: linear-gradient(180deg, #1c5fb8, #4d8ad6 55%, #d7e6f5 80%, #2a6cc4); }
  .thumb--concierge { left: 358px; }
  .thumb--concierge .thumb__image { background: radial-gradient(ellipse at 50% 60%, #9e9283, #4c4236 70%, #2c251d); }
  .thumb--doctors { left: 528px; }
  .thumb--doctors .thumb__image { background: linear-gradient(180deg, #cdc6bb, #efebe4 60%, #d9d3c8); }
  .thumb--signing { left: 698px; }
  .thumb--signing .thumb__image { background: linear-gradient(150deg, #ece4d6, #cfc2ad 60%, #9d8e78); }

  .site-footer { position: absolute; left: 187px; top: 626px; display: flex; align-items: center; gap: 14px; }
  .site-footer__brand { display: flex; align-items: center; gap: 4px; font-weight: 700; font-size: 15px; color: var(--text-light); }
  .site-footer__brand span.dot { width: 8px; height: 8px; border-radius: 50%; background: var(--text-light); }
  .site-footer__copy { font-size: 11px; color: var(--text-soft); }

  .social-links { position: absolute; top: 622px; left: 883px; display: flex; gap: 5px; }
  .social-links a {
    display: block; width: 33px; height: 33px; border-radius: 4px;
    background: linear-gradient(#a08a68, #7b6749);
    border: 1px solid rgba(255,255,255,.35);
  }
</style>
</head>
<body>
  <div class="corner-ornament corner-ornament--left" role="img" aria-label="Faint floral ornament along the page edge"></div>
  <div class="corner-ornament corner-ornament--right" role="img" aria-label="Faint floral ornament along the page edge"></div>

  <header>
    <div class="brand"><span class="brand__dot"></span><span class="brand__name">Vitalis</span></div>
    <div class="phone">416-555-018</div>

    <svg class="nav-ribbon" viewBox="0 0 978 56" aria-hidden="true">
      <defs>
        <linearGradient id="ribbonGold" x1="0" y1="0" x2="0" y2="1">
          <stop offset="0" stop-color="#d2ad70"/>
          <stop offset=".5" stop-color="#9c7440"/>
          <stop offset="1" stop-color="#6e4d25"/>
        </linearGradient>
        <linearGradient id="bandFill" x1="0" y1="0" x2="0" y2="1">
          <stop offset="0" stop-color="#7a6547"/>
          <stop offset="1" stop-color="#5f4d35"/>
        </linearGradient>
      </defs>
      <path d="M0 4 L60 12 L60 40 L8 34 L22 20 Z" fill="url(#ribbonGold)"/>
      <path d="M978 4 L918 12 L918 40 L970 34 L956 20 Z" fill="url(#ribbonGold)"/>
      <path d="M48 14 Q60 18 80 14 L80 52 Q62 56 48 50 Z" fill="url(#ribbonGold)"/>
      <path d="M930 14 Q918 18 898 14 L898 52 Q916 56 930 50 Z" fill="url(#ribbonGold)"/>
      <rect x="80" y="14" width="818" height="40" fill="url(#bandFill)"/>
      <line x1="80" y1="15" x2="898" y2="15" stroke="#c9a266" stroke-width="1"/>
    </svg>

    <nav class="main-nav">
      <a href="#" style="left:214px;width:113px">About Us</a>
      <a href="#" style="left:332px;width:112px">VIP Club</a>
      <a href="#" style="left:449px;width:113px">Services</a>
      <a href="#" style="left:566px;width:183px">Package and Prices</a>
      <a href="#" class="is-active" style="left:754px;width:112px">Registration</a>
      <a href="#" style="left:871px;width:112px">Contact</a>
    </nav>
  </header>

  <main>
    <section class="hero-frame">
      <div class="hero-photo" role="img" aria-label="Luxurious hotel suite with a large bed, drapes and chandelier"></div>
      <div class="hero-caption">
        <h1>VIP Club</h1>
        <p>Lorem Ipsum is simply dummy text of the<br>printing and typesetting industry</p>
      </div>
      <a class="slider-arrow slider-arrow--prev" href="#" aria-label="Previous slide">
        <svg width="20" height="20" viewBox="0 0 20 20"><path d="M16 2 L3 10 L16 18 Z" fill="#d8ccb6"/></svg>
      </a>
      <a class="slider-arrow slider-arrow--next" href="#" aria-label="Next slide">
        <svg width="20" height="22" viewBox="0 0 20 22"><path d="M3 1 L18 11 L3 21 Z" fill="#ffffff"/></svg>
      </a>
    </section>

    <section class="gallery-strip">
      <div class="thumb thumb--hospital"><div class="thumb__image" role="img" aria-label="Hospital building with emergency signage"></div></div>
      <div class="thumb thumb--flight"><div class="thumb__image" role="img" aria-label="Airliner flying through a blue sky"></div></div>
      <div class="thumb thumb--concierge"><div class="thumb__image" role="img" aria-label="Reception service bell on a desk"></div></div>
      <div class="thumb thumb--doctors"><div class="thumb__image" role="img" aria-label="Team of medical staff"></div></div>
      <div class="thumb thumb--signing"><div class="thumb__image" role="img" aria-label="Hand signing a document with a pen"></div></div>
    </section>
  </main>

  <footer class="site-footer">
    <div class="site-footer__brand"><span class="dot"></span>Vitalis</div>
    <p class="site-footer__copy">© Vitalis 2010. All rights reserved.</p>
  </footer>
  <div class="social-links">
    <a href="#" aria-label="Social profile"></a>
    <a href="#" aria-label="Social profile"></a>
    <a href="#" aria-label="News feed"></a>
  </div>
</body>
</html>
```